Website Design for recruiting company

We need a homepage mockup for a recruiting company focused on the legal industry. Use your creative talent to come up with something visually appeal and professional for this web-site.

We'd really like to see the maze from the logo incorporated into the design somehow. Please use the website mockup provided as inspiration for this project. We really like the layout and photos!

Target Market(s)

lawyers

Industry/Entity Type

Legal

Number of Pages Required

1 page

Font styles to use
Sans Serif

```html
<!DOCTYPE html>
<html lang="en">
<head>
<meta charset="utf-8">
<title>Harborline Legal Search</title>
<link href="https://fonts.googleapis.com/css2?family=Montserrat:wght@400;500;600;700&family=Open+Sans:ital,wght@0,400;0,600;1,400&display=swap" rel="stylesheet">
<style>
:root{
  --plum:#6f5f70;
  --plum-dark:#5e4f5f;
  --ink:#1b1b1b;
  --text:#5a5a5a;
  --muted:#8a8a8a;
  --light:#f2f2f2;
  --white:#ffffff;
  --line:#dcdcdc;
}
*{box-sizing:border-box;margin:0;padding:0}
html,body{width:1200px;height:3921px;overflow:hidden}
body{font-family:"Open Sans",sans-serif;color:var(--text);background:var(--white);position:relative}
a{color:inherit;text-decoration:none}

/* hero */
.hero{position:relative;height:633px;overflow:hidden}
.hero-photo{position:absolute;inset:0;background:linear-gradient(120deg,#6b574c 0%,#4a3d38 35%,#7d6a5e 60%,#3e332f 100%)}
.hero-photo::after{content:"";position:absolute;inset:0;background:rgba(30,22,25,.45)}
.nav{position:absolute;top:0;left:0;right:0;height:136px;display:flex;align-items:center;padding:0 20px;color:var(--white)}
.brand{display:flex;align-items:center;gap:14px;font-family:"Open Sans",sans-serif;font-size:15px;width:337px}
.brand-mark{width:97px;height:97px;border:3px solid var(--white);border-radius:50%}
.nav-links{display:flex;gap:36px;font-family:"Montserrat",sans-serif;font-size:15px;font-weight:500;align-items:center}
.nav-links svg{margin-left:2px}
.nav-cta{margin-left:auto;width:174px;height:46px;border:1.5px solid var(--white);border-radius:23px;display:flex;align-items:center;justify-content:center;font-family:"Montserrat",sans-serif;font-weight:600;font-size:15px}
.hero-title{position:absolute;top:240px;left:0;right:0;text-align:center;color:var(--white);font-family:"Montserrat",sans-serif;font-weight:500;font-size:50px;line-height:62px}
.hero-title strong{font-weight:700;font-size:64px}
.scroll-down{position:absolute;left:571px;top:549px;width:58px;height:58px;border:1.5px solid var(--white);border-radius:50%;display:flex;align-items:center;justify-content:center}

/* about */
.about{position:relative;height:592px}
.dot{position:absolute;border-radius:50%;background:#ececec}
.about-photo{position:absolute;left:122px;top:90px;width:412px;height:412px;border-radius:50%;background:linear-gradient(135deg,#d9d9d9,#9aa3ad 55%,#3b4a5e)}
.about-copy{position:absolute;left:600px;top:160px;width:480px}
.section-title{font-family:"Montserrat",sans-serif;font-weight:700;font-size:36px;color:var(--ink);letter-spacing:.5px}
.about-copy p{margin-top:22px;font-size:16px;line-height:34px;text-align:justify;color:#444}

/* jobs */
.news{background:var(--light);height:1895px;padding-top:76px}
.news .section-title{text-align:center}
.btn{display:block;width:146px;height:48px;border-radius:24px;margin:22px auto 0;background:var(--plum);color:var(--white);font-family:"Montserrat",sans-serif;font-weight:500;font-size:15px;line-height:48px;text-align:center}
.jobs{width:1022px;margin:32px auto 0;display:flex;flex-direction:column;gap:20px}
.job{height:301px;background:var(--white);display:flex}
.job.flip{flex-direction:row-reverse}
.job-tag{width:257px;flex:none;background:var(--plum);color:var(--white);padding:16px 14px}
.job-tag h3{font-family:"Montserrat",sans-serif;font-weight:700;font-size:26px;line-height:38px}
.job-meta{margin-top:24px;font-size:16px;line-height:34px}
.job-meta .id{font-family:"Montserrat",sans-serif;font-weight:600}
.job-meta span{display:flex;align-items:center;gap:14px}
.job-body{flex:1;padding:26px 22px;font-size:15px;line-height:30.5px;color:#555;text-align:justify}
.job.flip .job-body{padding:26px 76px 26px 27px}
.read-more{display:inline-block;margin-top:6px;font-family:"Montserrat",sans-serif;font-weight:600;font-size:15px;color:var(--plum);text-decoration:underline}

/* employers */
.employers{height:315px;background:var(--plum);color:var(--white);text-align:center;padding-top:58px}
.employers .section-title{color:var(--white)}
.employers p{font-size:18px;line-height:30px;margin:18px auto 0;width:660px}
.employers .btn{background:var(--white);color:var(--plum);margin-top:26px}

/* footer */
.footer{position:relative;height:486px;padding:0 89px}
.footer-brand{position:absolute;left:93px;top:96px;display:flex;align-items:center;gap:12px;width:1018px;font-size:14px;color:var(--muted)}
.footer-brand .brand-mark{width:90px;height:90px;border-color:#888}
.footer-brand::after{content:"";flex:1;height:1px;background:var(--line)}
.footer-col{position:absolute;top:206px}
.footer-col h4{font-family:"Montserrat",sans-serif;font-weight:500;font-size:18px;color:var(--plum)}
.about-blurb{left:89px;width:380px;top:212px;font-size:16px;line-height:30px;color:var(--muted)}
.follow{left:89px;top:318px}
.socials{display:flex;gap:18px;margin-top:18px}
.socials i{width:12px;height:12px;border-radius:50%;background:#999;display:block}
.links{left:582px}
.links ul,.contact ul{list-style:none;margin-top:16px;font-size:15px;line-height:30.5px;color:#666}
.contact{left:828px;width:290px}
.contact li{display:flex;gap:14px}
.contact svg{flex:none;margin-top:10px}
.footer-rule{position:absolute;left:89px;right:89px;top:432px;height:1px;background:var(--line)}
.copy{position:absolute;left:0;right:0;top:456px;text-align:center;font-size:12px;color:#888}
</style>
</head>
<body>

<header class="hero">
  <div class="hero-photo" role="img" aria-label="Two professionals in conversation seated in leather chairs in a bright office"></div>
  <nav class="nav">
    <div class="brand"><span class="brand-mark"></span>harborline legal search</div>
    <div class="nav-links">
      <a href="#">About Us</a><a href="#">What's New</a><a href="#">For Employers</a><a href="#">Regional</a><a href="#">Contact Us</a>
      <svg width="16" height="16" viewBox="0 0 16 16"><circle cx="6.5" cy="6.5" r="5" fill="none" stroke="#fff" stroke-width="2"/><line x1="10.5" y1="10.5" x2="15" y2="15" stroke="#fff" stroke-width="2.5"/></svg>
    </div>
    <a class="nav-cta" href="#">Submit Resume</a>
  </nav>
  <h1 class="hero-title"><strong>Start Here,</strong> Let Our<br>Experience Guide You</h1>
  <a class="scroll-down" href="#"><svg width="14" height="9" viewBox="0 0 14 9"><polyline points="1,1 7,7 13,1" fill="none" stroke="#fff" stroke-width="2"/></svg></a>
</header>

<section class="about">
  <span class="dot" style="left:210px;top:76px;width:72px;height:72px"></span>
  <span class="dot" style="left:74px;top:385px;width:118px;height:118px"></span>
  <span class="dot" style="left:466px;top:334px;width:118px;height:118px"></span>
  <div class="about-photo" role="img" aria-label="Smiling recruiter seated at a desk with documents"></div>
  <div class="about-copy">
    <h2 class="section-title">ABOUT US</h2>
    <p>Harborline Legal Search focuses on the permanent placement of attorneys with law firms and corporations in the New England area. Founded in 1982, Harborline Legal Search is the oldest attorney search firm in New England, and is ranked the number one legal recruiter in New England in the most recent survey conducted by <em>The Counsel Review.</em></p>
  </div>
</section>

<section class="news">
  <h2 class="section-title">WHAT’S NEW</h2>
  <a class="btn" href="#">Search Jobs</a>
  <div class="jobs">
    <article class="job">
      <div class="job-tag"><h3>IN-HOUSE/<br>CORPORATE/<br>M&amp;A</h3>
        <div class="job-meta"><span class="id"><svg width="12" height="13" viewBox="0 0 12 13"><circle cx="6" cy="3.5" r="3" fill="#fff"/><path d="M0 13c0-4 2.5-6 6-6s6 2 6 6z" fill="#fff"/></svg>Job Id &nbsp;: &nbsp;2772</span><span><svg width="12" height="12" viewBox="0 0 12 12"><rect x="0" y="2" width="12" height="10" fill="#fff"/></svg>Listing Date: 02/10/2020</span></div></div>
      <div class="job-body">Global exchange-listed medical technology leader seeks 8+ year M&amp;A specialist with major law firm training for lead role on all M&amp;A and other BD transactions. As a key member of the leadership team, this role will partner with the Vice President, Corporate Business Development to lead M&amp;A transactions from inception to closing and working effectively with Business Development, Corporate and Divisional Finance and Divisional Legal teams. Will be primarily dedicated to M&amp;A activity with responsibility for the negotiation, execution and all requisite legal support for strategic initiatives such as mergers and acquisitions, divestitures, licenses, alliances and collaborations, joint ventures and other.<br><a class="read-more" href="#">Read More</a></div>
    </article>
    <article class="job flip">
      <div class="job-tag"><h3>ASSOCIATE/<br>LITIGATION</h3>
        <div class="job-meta"><span class="id"><svg width="12" height="13" viewBox="0 0 12 13"><circle cx="6" cy="3.5" r="3" fill="#fff"/><path d="M0 13c0-4 2.5-6 6-6s6 2 6 6z" fill="#fff"/></svg>Job Id: 2778</span><span><svg width="12" height="12" viewBox="0 0 12 12"><rect x="0" y="2" width="12" height="10" fill="#fff"/></svg>Listing Date: 02/04/2020</span></div></div>
      <div class="job-body">Highly regarded mid-size national firm seeks litigation associate with 4-8 years of experience to join their Litigation Practice. This associate will work on a wide array of litigation matters including, construction, real estate, employment, shareholder and general business disputes. Fantastic opportunity to deal directly with clients and gain hands-on experience. Excellent work-life balance. Law firm experience preferred.</div>
    </article>
    <article class="job">
      <div class="job-tag"><h3>IN-HOUSE/<br>SENIOR<br>CORPORATE<br>COUNSEL/<br>SECURITIES</h3>
        <div class="job-meta" style="margin-top:10px"><span class="id"><svg width="12" height="13" viewBox="0 0 12 13"><circle cx="6" cy="3.5" r="3" fill="#fff"/><path d="M0 13c0-4 2.5-6 6-6s6 2 6 6z" fill="#fff"/></svg>Job Id: 2768</span><span><svg width="12" height="12" viewBox="0 0 12 12"><rect x="0" y="2" width="12" height="10" fill="#fff"/></svg>Listing Date: 01/29/2020</span></div></div>
      <div class="job-body">Leading Cambridge-based exchange-listed biotechnology company seeks 10+ year industry-experienced corporate/securities attorney for lead role in all public company matters and ongoing compliance, corporate governance, and corporate financing transactions. He/she will work closely with the executive team, business leadership, the legal, investor relations, human resources, finance, and business development departments, and outside counsel to further the Company’s ambitious agenda. This position offers exposure and involvement in a wide range of practice areas relevant to a high-growth, fast moving newly public platform-based biotechnology company.<br><a class="read-more" href="#">Read More</a></div>
    </article>
    <article class="job flip">
      <div class="job-tag"><h3>IN-HOUSE/<br>BIOTECH/<br>CONTRACTS</h3>
        <div class="job-meta"><span class="id"><svg width="12" height="13" viewBox="0 0 12 13"><circle cx="6" cy="3.5" r="3" fill="#fff"/><path d="M0 13c0-4 2.5-6 6-6s6 2 6 6z" fill="#fff"/></svg>Job Id: 2777</span><span><svg width="12" height="12" viewBox="0 0 12 12"><rect x="0" y="2" width="12" height="10" fill="#fff"/></svg>Listing Date: 01/28/2020</span></div></div>
      <div class="job-body" style="text-align:left">Outstanding opportunity for 3+ year attorney to join a premier biotech company in contracts counsel role. Prior experience drafting and negotiating biotech agreements including Clinical Trial Agreements, Master Service Agreements and related research and development contracts is required. Terrific opportunity to join highly collegial team with great work/life balance. Strong compensation.</div>
    </article>
    <article class="job">
      <div class="job-tag"><h3>IN-HOUSE /<br>LIFE SCIENCES /<br>SECURITIES</h3>
        <div class="job-meta"><span class="id"><svg width="12" height="13" viewBox="0 0 12 13"><circle cx="6" cy="3.5" r="3" fill="#fff"/><path d="M0 13c0-4 2.5-6 6-6s6 2 6 6z" fill="#fff"/></svg>Job Id: 2773</span><span><svg width="12" height="12" viewBox="0 0 12 12"><rect x="0" y="2" width="12" height="10" fill="#fff"/></svg>Listing Date: 01/14/2020</span></div></div>
      <div class="job-body" style="text-align:left;padding-right:120px">Terrific opportunity for 3rd – 6th year corporate attorney to join outstanding MA-based exchange-listed biopharmaceutical company. Major firm and strong securities and corporate governance experience required, including demonstrated knowledge of U.S. securities law and experience coordinating filings and disclosures. M&amp;A and/or licensing experience a plus. Stellar legal team and strong compensation.</div>
    </article>
  </div>
</section>

<section class="employers">
  <h2 class="section-title">FOR EMPLOYERS</h2>
  <p>Our unparalleled recruiting industry and legal experience have generated an extensive network of contacts throughout the legal community.</p>
  <a class="btn" href="#">Start Here</a>
</section>

<footer class="footer">
  <div class="footer-brand"><span class="brand-mark"></span>harborline legal search</div>
  <p class="footer-col about-blurb">Lorem ipsum dolor sit amet, consectetur adipiscing elit, sed do eiusmod tempor incididunt ut labore et dolore magna aliqua.</p>
  <div class="footer-col follow"><h4>Follow Us</h4><div class="socials"><i></i><i></i><i></i><i></i><i></i></div></div>
  <div class="footer-col links"><h4>Links</h4>
    <ul><li>About Us</li><li>What's New</li><li>For Employers</li><li>Regional</li><li>Contact Us</li></ul></div>
  <div class="footer-col contact"><h4>Contact Us</h4>
    <ul>
      <li><svg width="10" height="13" viewBox="0 0 10 13"><path d="M5 0a5 5 0 0 0-5 5c0 4 5 8 5 8s5-4 5-8a5 5 0 0 0-5-5z" fill="#555"/><circle cx="5" cy="5" r="1.8" fill="#fff"/></svg>Harborline Legal Search, P.O. Box 41820, Cedar Harbor MA 01999</li>
      <li><svg width="12" height="12" viewBox="0 0 12 12"><path d="M2 0l3 3-1.5 2a8 8 0 0 0 3.5 3.5L9 7l3 3-2 2C5 12 0 7 0 2z" fill="#555"/></svg>Tel: 555.010.2040</li>
      <li><svg width="12" height="12" viewBox="0 0 12 12"><rect x="0" y="4" width="12" height="8" fill="#555"/><rect x="3" y="0" width="6" height="4" fill="#555"/></svg>Fax: 555.010.2041</li>
      <li><svg width="12" height="10" viewBox="0 0 12 10"><rect width="12" height="10" fill="#555"/><polyline points="0,0 6,5 12,0" fill="none" stroke="#fff"/></svg>info@harborlinelegal.com</li>
    </ul></div>
  <div class="footer-rule"></div>
  <p class="copy">© 2020 The Company Name. All rights Reserved.</p>
</footer>

</body>
</html>
```